Business Card Design Project

I am a Chiropractor that is looking for a new business card.  Our logo was slightly changed lately, therefore need a new, more professional look.
We are a modern, non-stuffy chiropractic office.  Want a contemporary look that will let people know this is not your typical doctors office.  Our logo is red, and contains the name of our business: realign.  The u in the logo is green, stressing the most important part of our business: "u"

Target Market(s)
moderate to upper income bracket, family friendly
www.realignspine-example.com
Gordon Pell
Family Chiropractor
314 Hollis Rd
Bastrop, TX 78999
512.555.0147 phone
512.555.0148 fax
Industry/Entity Type
Business
Requirements
Must have
- www.realignspine-example.com
Gordon Pell
Family Chiropractor
314 Hollis Rd
Bastrop, TX 78999
512.555.0147 phone
512.555.0148 fax

```html
<!DOCTYPE html>
<html lang="en">
<head>
<meta charset="UTF-8">
<title>realign – Business Card</title>
<link rel="stylesheet" href="https://fonts.googleapis.com/css2?family=Source+Sans+3:wght@400;600&display=swap">
<style>
  :root {
    --canvas: #ffffff;
    --card: #f4f4f4;
    --brand-red: #e8413a;
    --brand-green: #6db33f;
    --ink: #5a5a5a;
    --white: #ffffff;
  }
  html, body {
    margin: 0;
    padding: 0;
    width: 1200px;
    height: 900px;
    overflow: hidden;
    background: var(--canvas);
    font-family: "Source Sans 3", Arial, sans-serif;
  }
  .stage {
    position: relative;
    width: 1200px;
    height: 900px;
  }
  .card {
    position: absolute;
    width: 434px;
    height: 760px;
    background: var(--card);
    border-radius: 32px;
    overflow: hidden;
  }
  .card--top-band {
    left: 140px;
    top: 44px;
    box-shadow: 0 6px 14px rgba(0,0,0,0.22);
  }
  .card--bottom-band {
    left: 706px;
    top: 56px;
    box-shadow: 0 8px 16px rgba(0,0,0,0.32);
  }
  .brand {
    position: absolute;
    left: 0;
    right: 0;
    text-align: center;
    font-size: 88px;
    font-weight: 400;
    line-height: 1;
    color: var(--brand-red);
    letter-spacing: 1px;
  }
  .card--top-band .brand { top: 90px; }
  .card--bottom-band .brand { top: 88px; }
  .web-band {
    position: absolute;
    left: 0;
    right: 0;
    background: var(--brand-green);
    color: var(--white);
    text-align: center;
    font-size: 25px;
    letter-spacing: 0.5px;
  }
  .card--top-band .web-band {
    top: 266px;
    height: 50px;
    line-height: 50px;
  }
  .card--bottom-band .web-band {
    bottom: 0;
    height: 66px;
    line-height: 60px;
  }
  .contact {
    position: absolute;
    left: 42px;
    color: var(--ink);
  }
  .card--top-band .contact { top: 372px; }
  .card--bottom-band .contact { top: 334px; }
  .contact__name {
    margin: 0;
    font-size: 31px;
    font-weight: 600;
    color: var(--brand-red);
    line-height: 36px;
  }
  .contact__role {
    margin: 0 0 8px;
    font-size: 24px;
    color: var(--brand-green);
    line-height: 30px;
  }
  .contact__lines {
    margin: 0 0 8px;
    font-size: 23px;
    line-height: 29px;
  }
</style>
</head>
<body>
<main class="stage">
  <section class="card card--top-band" aria-label="Business card, web band under the name mark">
    <div class="brand">realign</div>
    <div class="web-band">www.realignspine-example.com</div>
    <div class="contact">
      <p class="contact__name">GORDON PELL</p>
      <p class="contact__role">Family Chiropractor</p>
      <p class="contact__lines">314 Hollis Rd<br>Bastrop, TX 78999</p>
      <p class="contact__lines">512.555.0147 phone<br>512.555.0148 fax</p>
    </div>
  </section>

  <section class="card card--bottom-band" aria-label="Business card, web band at the foot">
    <div class="brand">realign</div>
    <div class="contact">
      <p class="contact__name">GORDON PELL</p>
      <p class="contact__role">Family Chiropractor</p>
      <p class="contact__lines">314 Hollis Rd<br>Bastrop, TX 78999</p>
      <p class="contact__lines">512.555.0147 phone<br>512.555.0148 fax</p>
    </div>
    <div class="web-band">www.realignspine-example.com</div>
  </section>
</main>
</body>
</html>
```